Kestrel Summit 2019 Enemies of the End-Times Church Flyer

We want a church conference flyer designed. We are looking for a professional, yet catchy design that uses our brand colors and logo creatively while communicating key information of the event effectively. <br/>The flyer must include all of the following:<br/>Title: Kestrel Summit 2019<br/>Topic: The Enemies of The End-Times Church <br/>Subtitles: <br/> -How the antichrist raises an army by social behavior engineering. <br/>-How the architects of modern social constructs escaped the church's radar. <br/>-The Holy Spirit's end-times agenda:<br/> The Knock-Out Punch!<br/>Speaker: Prophet Marcus Toliver <br/>Dates/time: December 27, 28 & 29 at 6pm<br/>Location: Halvorn Community Center <br/> 241 Pellham Street <br/> Portland, ME 04102<br/>Contact info: phone: 207-555-0148 <br/>email: contact@brookmeadow.example <br/> www.vutel.example<br/>*The flyer must also include a picture of the speaker and our Vutel logo <br/>Thanks, we look forward to seeing what you come up with!

Colors

Designer to choose colors to be used in the design.

Requirements
Must have
• The flyer must include all of the following:
• Title: Kestrel Summit 2019
• Topic: The Enemies of The End-Times Church
• Subtitles:
• -How the antichrist raises an army by social behavior engineering.
• -How the architects of modern social constructs escaped the church's radar.
• -The Holy Spirit's end-times agenda:
• The Knock-Out Punch!
• Speaker: Prophet Marcus Toliver
• Dates/time: December 27, 28 & 29 at 6pm
• Location: Halvorn Community Center
• 241 Pellham Street
• Portland, ME 04102
• Contact info: phone: 207-555-0148
• email: contact@brookmeadow.example
• www.vutel.example
• *The flyer must also include a picture of the speaker and our Vutel logo
Should not have
• Pictures of crosses or church buildings

```html
<!DOCTYPE html>
<html lang="en">
<head>
<meta charset="utf-8">
<title>Kestrel Summit 2019 – Flyer</title>
<link rel="stylesheet" href="https://fonts.googleapis.com/css2?family=Lexend:wght@400;500;600&family=Yellowtail&display=swap">
<style>
  :root {
    --orange: #f7931e;
    --navy: #12365b;
    --white: #ffffff;
    --paper: #f2f2f2;
    --ink: #1c2a3a;
    --photo-top: #5b6f88;
    --photo-bottom: #9fb3cc;
  }
  * { margin: 0; padding: 0; box-sizing: border-box; }
  html, body {
    width: 1200px; height: 1200px; overflow: hidden;
    background: var(--paper);
    font-family: "Lexend", sans-serif;
  }
  .flyer {
    position: absolute; left: 170px; top: 51px;
    width: 790px; height: 1009px;
    background: var(--white);
    transform: scale(1.0886); transform-origin: 0 0;
    overflow: hidden;
    box-shadow: 0 4px 18px rgba(0,0,0,.12);
  }
  .header {
    position: absolute; left: 0; top: 0; width: 790px; height: 327px;
    background: var(--orange);
  }
  .topic {
    position: absolute; left: 48px; top: 58px;
    color: var(--navy); font-weight: 600; font-size: 47px; line-height: 60px;
    letter-spacing: -0.3px;
  }
  .summit-title {
    position: absolute; left: 488px; top: 40px; width: 270px;
    text-align: center;
    font-family: "Yellowtail", cursive;
    font-weight: 400;
    color: var(--navy);
    font-size: 64px; line-height: 62px;
    transform: rotate(-4deg);
    text-shadow:
      2px 0 0 var(--white), -2px 0 0 var(--white),
      0 2px 0 var(--white), 0 -2px 0 var(--white),
      1.5px 1.5px 0 var(--white), -1.5px -1.5px 0 var(--white),
      1.5px -1.5px 0 var(--white), -1.5px 1.5px 0 var(--white);
  }
  .summit-title span { display: block; }
  .summit-title .line-1 { padding-left: 40px; }
  .summit-title .line-3 { padding-left: 60px; }
  .subtitles {
    position: absolute; left: 48px; top: 249px;
    color: var(--white); font-size: 16.5px; line-height: 28px; font-weight: 400;
  }
  .edge {
    position: absolute; left: 0; width: 790px; height: 6px;
    background:
      linear-gradient(135deg, var(--c) 3px, transparent 0) 0 0 / 6px 6px repeat-x,
      linear-gradient(225deg, var(--c) 3px, transparent 0) 0 0 / 6px 6px repeat-x;
  }
  .edge--orange { top: 326px; --c: var(--orange); }
  .edge--navy { top: 418px; --c: var(--navy); transform: scaleY(-1); }
  .agenda {
    position: absolute; left: 0; top: 345px; width: 790px;
    text-align: center; color: var(--navy);
    font-weight: 500; font-size: 21px; line-height: 31px;
  }
  .speaker-band { position: absolute; left: 0; top: 0; }
  .speaker {
    position: absolute; left: 48px; top: 536px; color: var(--white);
  }
  .speaker-label { font-size: 22px; font-weight: 500; }
  .speaker-name { font-size: 33px; font-weight: 600; margin-top: 10px; letter-spacing: -0.3px; white-space: nowrap; }
  .info {
    position: absolute; color: var(--ink);
    font-size: 16.5px; line-height: 22px; font-weight: 400;
  }
  .info strong { font-weight: 600; }
  .info--location { left: 48px; top: 742px; }
  .info--contact { left: 48px; top: 868px; }
  .info--dates { left: 492px; top: 742px; }
  .brand {
    position: absolute; left: 506px; top: 872px;
    display: flex; align-items: center; gap: 12px;
  }
  .brand-mark { width: 26px; height: 26px; border-radius: 50%; background: var(--orange); }
  .brand-name { color: var(--navy); font-size: 58px; font-weight: 500; line-height: 1; }
  .footer-bar {
    position: absolute; left: 0; top: 967px; width: 790px; height: 42px;
    background: var(--orange);
  }
</style>
</head>
<body>
  <main class="flyer">
    <section class="header">
      <h1 class="topic">The Enemies of<br>The End-Times<br>Church</h1>
      <h2 class="summit-title"><span class="line-1">Kestrel</span><span class="line-2">Summit</span><span class="line-3">2019</span></h2>
      <p class="subtitles">How the antichrist raises an army by social behavior engineering.<br>How the architects of modern social constructs escaped the church's radar.</p>
    </section>
    <div class="edge edge--orange"></div>

    <p class="agenda">The Holy Spirit's end-times agenda:<br>The Knock-Out Punch!</p>

    <svg class="speaker-band" width="790" height="760" viewBox="0 0 790 760">
      <defs>
        <linearGradient id="photoTone" x1="0" y1="0" x2="0" y2="1">
          <stop offset="0" stop-color="#5b6f88"/>
          <stop offset="1" stop-color="#9fb3cc"/>
        </linearGradient>
      </defs>
      <polygon points="0,423 790,423 790,607 483,692 463,620 0,742" fill="#12365b"/>
      <polygon points="466,440 738,440 738,620 483,692 463,620" fill="url(#photoTone)" role="img" aria-label="Photo of the speaker, Prophet Marcus Toliver, speaking at a microphone"/>
      <polyline points="0,742 463,620 483,692 790,607" fill="none" stroke="#f7931e" stroke-width="5"/>
    </svg>
    <div class="edge edge--navy"></div>

    <div class="speaker">
      <p class="speaker-label">Speaker:</p>
      <p class="speaker-name">Prophet Marcus Toliver</p>
    </div>

    <p class="info info--location"><strong>Location:</strong><br>Halvorn Community Center<br>241 Pellham Street<br>Portland, ME 04102</p>
    <p class="info info--contact"><strong>Contact:</strong><br>Phone: 207-555-0148<br>Email: contact@brookmeadow.example<br>Website: www.vutel.example</p>
    <p class="info info--dates"><strong>Dates:</strong><br>27, 28 &amp; 29 December, 2019<br><strong>Time:</strong> 6pm</p>

    <div class="brand">
      <span class="brand-mark"></span>
      <span class="brand-name">Vutel</span>
    </div>

    <div class="footer-bar"></div>
  </main>
</body>
</html>
```